Outpatient imaging center needs a flyer design

Flyer must include the provided logo.
Orange/Yellow color is being included
MRI scanner image-
A4, Z fold, 6 pages-double sized

Industry/Entity Type

healthcare

Colors
F0912C
F2A743
F7CA91
FBE8D2
FDF5EE

```html
<!DOCTYPE html>
<html lang="en">
<head>
<meta charset="utf-8">
<title>Lumora MRI – Outpatient Imaging Flyer</title>
<link href="https://fonts.googleapis.com/css2?family=Roboto:wght@400;500;700&display=swap" rel="stylesheet">
<style>
:root{
  --orange:#F0912C;
  --orange-mid:#F2A743;
  --orange-soft:#F7CA91;
  --cream:#FBE8D2;
  --ivory:#FDF5EE;
  --ink:#1d1d1d;
  --body:#333;
  --panel-grey:#959595;
  --shape-grey:#b3b3b3;
  --backdrop:#dedede;
  --black:#000;
}
*{margin:0;padding:0;box-sizing:border-box}
html,body{width:1200px;height:851px;overflow:hidden;background:var(--backdrop);font-family:"Roboto",Arial,sans-serif;color:var(--body)}
.page{position:absolute;top:72px;width:500px;height:707px;background:#fff;overflow:hidden}
.page--front{left:72px}
.page--inside{left:628px}
.abs{position:absolute}
.brand{position:absolute;top:26px;font-size:17px;font-weight:500;letter-spacing:.5px;color:var(--orange);white-space:nowrap;display:flex;align-items:center;gap:6px}
.brand__dot{width:12px;height:12px;border-radius:50%;background:var(--orange)}
.page--front .brand{left:36px}
.page--inside .brand{right:50px}
.photo{position:absolute;border-radius:50%}
.headline{font-weight:700;color:var(--ink);text-transform:uppercase;letter-spacing:.2px}
.body-text{font-size:7.2px;line-height:10.3px;color:var(--body)}
.icon-badge{position:absolute;width:28px;height:28px;border-radius:50%;background:var(--orange);display:flex;align-items:center;justify-content:center}
.feature{position:absolute;width:130px}
.feature__title{font-size:8.3px;font-weight:500;letter-spacing:.6px;color:var(--ink);line-height:10.5px;text-transform:uppercase}
.feature__text{font-size:5.8px;line-height:9px;color:var(--body);margin-top:4px}
.footer{position:absolute;left:0;bottom:0;width:500px;height:31px}
.footer__rule{height:4px;background:#9a9a9a}
.footer__bar{height:27px;background:var(--black);display:flex;align-items:center;justify-content:center;gap:10px;color:#fff}
.footer__cta{font-size:8.4px;font-weight:500;letter-spacing:.2px}
.footer__phone-icon{width:18px;height:18px;border-radius:50%;background:var(--orange);display:flex;align-items:center;justify-content:center}
.footer__number{font-size:11px;font-weight:500;letter-spacing:.4px}
.intro-panel{position:absolute;left:177px;top:75px;width:323px;height:219px;background:var(--panel-grey)}
.intro-title{position:absolute;left:257px;top:108px;font-size:13px;line-height:18px;font-weight:500;color:#fff}
.intro-text{position:absolute;left:257px;top:167px;width:194px;font-size:5.9px;line-height:10.1px;color:#fff;text-align:justify}
.section-title{position:absolute;left:29px;font-size:12px;font-weight:500;color:var(--ink);letter-spacing:.3px}
.sub-title{position:absolute;left:29px;font-size:8.3px;font-weight:500;color:var(--orange);text-decoration:underline;letter-spacing:.4px}
.service{position:absolute;top:498px;width:104px}
.service .icon-badge{position:relative}
.service__title{margin-top:11px;font-size:8.2px;line-height:10.4px;font-weight:500;color:var(--ink);letter-spacing:.2px}
.ticks{list-style:none;margin-top:4px}
.ticks li{font-size:5.8px;line-height:11.1px;color:var(--body);display:flex;align-items:center;gap:8px}
.ticks li::before{content:"";width:5px;height:5px;border:1px solid var(--orange);border-radius:1px;flex:none;background:
 linear-gradient(45deg,transparent 40%,var(--orange) 40%,var(--orange) 60%,transparent 60%)}
.ticks--offset{margin-top:-9px}
</style>
</head>
<body>

<!-- Front page -->
<section class="page page--front">
  <svg class="abs" style="left:0;top:0" width="500" height="440" viewBox="0 0 500 440">
    <path d="M500,0 L430,0 C405,30 404,90 410,150 C416,225 414,292 368,330 L398,412 C440,410 476,396 500,382 Z" fill="var(--shape-grey)"/>
    <path d="M500,12 C455,40 425,110 432,190 C438,250 432,300 382,330 C334,356 292,346 280,345 C302,392 342,412 382,409 C432,405 470,382 500,360 Z" fill="var(--orange)"/>
    <circle cx="290" cy="222" r="182" fill="none" stroke="var(--orange)" stroke-width="1.6"/>
    <circle cx="387" cy="67" r="20" fill="var(--orange)"/>
    <circle cx="124" cy="146" r="10" fill="var(--orange)"/>
    <circle cx="287" cy="224" r="146" fill="#8a8a8a"/>
  </svg>
  <div class="photo" style="left:151px;top:70px;width:288px;height:288px;background:radial-gradient(circle at 55% 45%,#f4f9fd 0%,#cfe4f2 45%,#6fa4c6 100%)" role="img" aria-label="Photo of a modern MRI scanner with patient table in a bright clinic room"></div>

  <div class="brand"><span class="brand__dot"></span>LUMORA MRI</div>

  <h1 class="headline abs" style="left:28px;top:429px;font-size:12.4px;line-height:15.4px;width:440px">Lumora MRI, LLC acquires breakthrough Veranta MR scanner designed to improve confidence, speed, and comfort</h1>
  <p class="body-text abs" style="left:28px;top:468px;width:430px">Hello and thank you for your interest in our Lumora MRI imaging services. At Lumora MRI, we specialize in advanced MRI screenings that can provide valuable insights into your heart health and overall whole-body well-being. Today, I'd like to share some information about our cardiac MRI screening and whole-body MRI screening services.</p>

  <h2 class="headline abs" style="left:28px;top:515px;font-size:12px">Why choose Lumora MRI?</h2>
  <p class="body-text abs" style="left:28px;top:534px;width:430px">At Lumora MRI, we prioritize patient comfort, safety, and accurate diagnostics. Here are a few reasons why you should consider us for your MRI screening needs:</p>

  <div class="icon-badge" style="left:28px;top:559px"><svg width="14" height="14" viewBox="0 0 14 14"><circle cx="7" cy="5" r="3" fill="none" stroke="#fff" stroke-width="1.2"/><path d="M2 13c1-3 3-4 5-4s4 1 5 4" fill="none" stroke="#fff" stroke-width="1.2"/></svg></div>
  <div class="feature" style="left:28px;top:594px"><div class="feature__title">Expertise</div><p class="feature__text">Our team consists of skilled Cardiac MRI technologists with over a decade of experience and radiologists specializing in cardiac and whole-body imaging.</p></div>

  <div class="icon-badge" style="left:177px;top:559px"><svg width="14" height="14" viewBox="0 0 14 14"><circle cx="7" cy="7" r="5" fill="none" stroke="#fff" stroke-width="1.4" stroke-dasharray="2 1.2"/><circle cx="7" cy="7" r="2" fill="#fff"/></svg></div>
  <div class="feature" style="left:177px;top:594px"><div class="feature__title">Special software and<br>state-of-the-art<br>technology</div><p class="feature__text">We utilize cutting-edge MRI equipment together with the dedicated cardiac software to ensure high-quality images and precise diagnoses.</p></div>

  <div class="icon-badge" style="left:326px;top:559px"><svg width="14" height="14" viewBox="0 0 14 14"><circle cx="7" cy="4" r="2" fill="#fff"/><path d="M1 8l3 4h6l3-4" fill="none" stroke="#fff" stroke-width="1.3"/></svg></div>
  <div class="feature" style="left:326px;top:594px;width:130px"><div class="feature__title">Personalized care</div><p class="feature__text">We understand the importance of personalized healthcare, and our staff will guide you through every step of the screening process.</p></div>

  <footer class="footer"><div class="footer__rule"></div><div class="footer__bar"><span class="footer__cta">CALL NOW TO BOOK YOUR APPOINTMENT!</span><span class="footer__phone-icon"><svg width="9" height="9" viewBox="0 0 10 10"><path d="M2 1l2 2-1 1.5c.6 1.2 1.3 1.9 2.5 2.5L7 6l2 2-1.2 1.3C4.5 9 1 5.5.7 2.2Z" fill="#fff"/></svg></span><span class="footer__number">555 014 2270</span></div></footer>
</section>

<!-- Inside page -->
<section class="page page--inside">
  <div class="intro-panel"></div>
  <svg class="abs" style="left:0;top:0" width="260" height="340" viewBox="0 0 260 340">
    <circle cx="103" cy="185" r="143" fill="#fff"/>
    <circle cx="103" cy="185" r="140" fill="none" stroke="var(--orange)" stroke-width="1.6"/>
  </svg>
  <div class="photo" style="left:-28px;top:54px;width:262px;height:262px;background:radial-gradient(circle at 45% 55%,#eef6fb 0%,#bcd9ea 50%,#7fb0cf 100%)" role="img" aria-label="Photo of a wide-bore MRI scanner with control display and patient bed"></div>

  <div class="brand"><span class="brand__dot"></span>LUMORA MRI</div>

  <h2 class="intro-title">ROUTINE SERVICES-FOR<br>PATIENTS</h2>
  <svg class="abs" style="left:224px;top:151px" width="74" height="8" viewBox="0 0 74 8"><line x1="0" y1="4" x2="70" y2="4" stroke="var(--orange)" stroke-width="1"/><circle cx="70" cy="4" r="3.8" fill="var(--orange)"/></svg>
  <p class="intro-text">Welcome to Lumora MRI Imaging Center, where cutting-edge technology meets compassionate care! With over a decade of experience as an MRI technologist, I've seen firsthand the challenges patients face when trying to access quality MRI exams. At Lumora, we're committed to revolutionizing your imaging experience. We understand the struggles individuals encounter, especially those needing larger accommodations due to implanted devices or seeking flexibility in scheduling. That's why our center boasts the next generation of MRI scanners, featuring an expansive wide bore designed to provide comfortabilities.</p>

  <h2 class="section-title" style="top:357px">OUR MISSION</h2>
  <p class="body-text abs" style="left:29px;top:381px;width:450px">At Lumora MRI, our mission is to provide exceptional MRI imaging services with a focus on accuracy, safety, and patient-centered care.</p>

  <h2 class="section-title" style="top:405px">ROUTINE SERVICES</h2>
  <div class="sub-title" style="top:428px">INSURANCE USERS</div>
  <p class="body-text abs" style="left:29px;top:442px">Prior authorization and a physician's order are required for MRI services.</p>
  <div class="sub-title" style="top:460px">CASH PAYMENTS</div>
  <p class="body-text abs" style="left:29px;top:474px">No physician's order is necessary for cash-only screenings. You have the freedom to select your preferred area of focus:</p>

  <div class="service" style="left:29px">
    <div class="icon-badge"><svg width="14" height="14" viewBox="0 0 14 14"><circle cx="7" cy="7" r="5" fill="none" stroke="#fff" stroke-width="1.4"/><rect x="2" y="8" width="10" height="2" fill="#fff"/></svg></div>
    <div class="service__title">MRI HEAD, NECK,<br>SPINE</div>
    <ul class="ticks"><li>Brain</li><li>Brain Orbits</li><li>Cervical spine</li><li>Thoracic spine</li><li>Lumbar spine</li></ul>
  </div>
  <div class="service" style="left:134px">
    <div class="icon-badge"><svg width="14" height="14" viewBox="0 0 14 14"><rect x="2" y="2" width="10" height="10" rx="1" fill="none" stroke="#fff" stroke-width="1.3"/><line x1="7" y1="3.5" x2="7" y2="10.5" stroke="#fff"/><line x1="4" y1="6" x2="10" y2="6" stroke="#fff"/><line x1="4" y1="8.5" x2="10" y2="8.5" stroke="#fff"/></svg></div>
    <div class="service__title">MRI CHEST, ABDOMEN,<br>PELVIS</div>
    <ul class="ticks"><li>Chest</li><li>Abdomen</li><li>Enterography</li><li>Pelvis</li><li>Brachial plexus</li></ul>
  </div>
  <div class="service" style="left:240px">
    <div class="icon-badge"><svg width="14" height="14" viewBox="0 0 14 14"><circle cx="7" cy="6" r="4.5" fill="none" stroke="#fff" stroke-width="1.3"/><rect x="2" y="10" width="10" height="2" fill="#fff"/></svg></div>
    <div class="service__title">MRI MSK</div>
    <ul class="ticks"><li>Shoulder,</li><li>Elbow,</li><li>Wrist,</li><li>Knee,</li><li>Ankle</li><li>Foot</li><li>Humerus</li><li>Forearm</li><li>Femur</li><li>Lower Leg</li></ul>
  </div>
  <div class="service" style="left:345px;width:130px">
    <div class="icon-badge"><svg width="14" height="14" viewBox="0 0 14 14"><rect x="2" y="2" width="8" height="6" fill="none" stroke="#fff" stroke-width="1.2"/><path d="M6 8v3h5V5" fill="none" stroke="#fff" stroke-width="1.2"/></svg></div>
    <div class="service__title">MR ANGIOGRAPHY,<br>VENOGRAPHY, CARDIAC</div>
    <ul class="ticks"><li>Head w/o MRA or MRV</li><li>Head w/ MRA or MRV</li><li>Head w/ and w/o MRA or MRV</li><li>Neck w/o MRA or MRV</li><li>Neck w/ MRA or MRV</li><li>Abdomen MRA or MRV</li><li>Pelvis MRA or MRV</li><li>Lower extremity MRA or MRV</li><li>Upper extremity MRA or MRV</li></ul>
  </div>

  <footer class="footer"><div class="footer__rule"></div><div class="footer__bar"><span class="footer__cta">CALL NOW TO BOOK YOUR APPOINTMENT!</span><span class="footer__phone-icon"><svg width="9" height="9" viewBox="0 0 10 10"><path d="M2 1l2 2-1 1.5c.6 1.2 1.3 1.9 2.5 2.5L7 6l2 2-1.2 1.3C4.5 9 1 5.5.7 2.2Z" fill="#fff"/></svg></span><span class="footer__number">555 014 2270</span></div></footer>
</section>

</body>
</html>
```